Net Clarity Partners Needs a New Business Card Design

Attached is my new logo that ArtFolkHub created and picture of me for the back of the business card. Also attached is the information to include on the business card (on my existing business card design - QZR4 file attached).

The designer also provided a treatment of my logo that I really like if you can use it somehow. Also attached - file name "Preferred Version of New Logo."

Maren Falstead

Net Clarity Partners
4517 Pellam Rd., #349
Houston, TX 77348

Tel: (832) 555-0147
www.netclaritypartners.example
maren@netclaritypartners.example

Thank you.

Reason: I'm close but am having a hard time deciding.

Target Market(s)

attorneys and law firms

Industry/Entity Type

Legal

Contact Information for Business Card

Proved in the Project Description

Font styles to use
Other font styles liked:
• I am open on font - no script though.

Colors
2d73b3
33a6d7

Requirements
Must have
• my logo
• company name & contact info
• my picture on the back
• colors that coordinate with the logo
Nice to have
• love to use the treated version of the logo if possible

```html
<!DOCTYPE html>
<html lang="en">
<head>
<meta charset="utf-8">
<title>Net Clarity Partners – Business Card</title>
<link href="https://fonts.googleapis.com/css2?family=Montserrat:wght@400;500;700&display=swap" rel="stylesheet">
<style>
  :root{
    --bg:#2a2a2c;
    --paper:#ffffff;
    --paper-shade:#e9ecef;
    --slate:#253038;
    --slate-deep:#1a2228;
    --slate-light:#3a4750;
    --blue:#33a6d7;
    --blue-dark:#2d73b3;
    --ink-soft:#c9d1d6;
    --grey:#8e979d;
  }
  *{box-sizing:border-box;margin:0;padding:0}
  html,body{width:1200px;height:997px;overflow:hidden}
  body{background:var(--bg);font-family:"Montserrat",Arial,sans-serif;position:relative}

  .card{position:absolute;width:560px;height:320px;border-radius:16px;overflow:hidden;
        box-shadow:0 18px 40px rgba(0,0,0,.55)}

  /* Front */
  .card--front{left:80px;top:110px;background:var(--slate)}
  .front__top{position:absolute;left:0;top:0;width:100%;height:138px;
              background:linear-gradient(180deg,var(--paper) 0%,var(--paper-shade) 100%);
              display:flex;flex-direction:column;align-items:center;justify-content:center}
  .front__rule{position:absolute;left:0;top:138px;width:100%;height:5px;background:var(--blue)}
  .front__notch{position:absolute;left:46px;top:142px;width:0;height:0;
                border-left:9px solid transparent;border-right:9px solid transparent;
                border-top:10px solid var(--blue)}
  .brand-name{font-weight:700;font-size:28px;letter-spacing:1px;color:var(--blue);text-transform:uppercase}
  .brand-tagline{margin-top:6px;font-weight:500;font-size:10.5px;letter-spacing:3.2px;color:var(--grey);text-transform:uppercase}

  .holder{position:absolute;left:46px;top:166px}
  .holder__name{font-size:20px;font-weight:400;color:var(--blue)}
  .holder__role{font-size:11px;font-weight:700;color:var(--paper);margin-top:3px}

  .contact{position:absolute;left:46px;top:228px;list-style:none}
  .contact__item{display:flex;align-items:center;gap:10px;font-size:13px;color:var(--ink-soft);height:24px}
  .contact__icon{width:13px;height:13px;fill:var(--blue)}

  /* Back */
  .card--back{left:560px;top:520px;
              background:radial-gradient(ellipse at 70% 30%,var(--slate-light) 0%,var(--slate) 55%,var(--slate-deep) 100%)}
  .back__portrait{position:absolute;left:22px;top:40px;width:220px;height:222px;border-radius:110px 110px 0 0;
                  background:linear-gradient(180deg,#c9a27a 0%,#d8b08f 45%,#4a3f9e 75%,#3d3390 100%)}
  .back__brand{position:absolute;left:270px;top:92px;width:270px;text-align:center}
  .back__brand .brand-name{font-size:24px}
  .back__brand .brand-tagline{font-size:9px;letter-spacing:2.6px;color:var(--ink-soft)}
  .back__rule{position:absolute;left:0;top:258px;width:100%;height:5px;background:var(--blue)}
  .back__notch{position:absolute;left:328px;top:249px;width:0;height:0;
               border-left:9px solid transparent;border-right:9px solid transparent;
               border-bottom:10px solid var(--blue)}
  .back__band{position:absolute;left:0;top:263px;width:100%;height:57px;background:var(--slate-deep);
              display:flex;align-items:center;justify-content:center}
  .back__url{font-size:17px;font-weight:500;letter-spacing:2.6px;color:var(--ink-soft)}
</style>
</head>
<body>

<section class="card card--front" aria-label="Business card front">
  <div class="front__top">
    <div class="brand-name">Net Clarity Partners</div>
    <div class="brand-tagline">Smart Marketing for Law Firms</div>
  </div>
  <div class="front__rule"></div>
  <div class="front__notch"></div>

  <div class="holder">
    <div class="holder__name">Maren Falstead</div>
    <div class="holder__role">Owner</div>
  </div>

  <ul class="contact">
    <li class="contact__item">
      <svg class="contact__icon" viewBox="0 0 24 24" aria-hidden="true"><path d="M6.6 10.8a15.1 15.1 0 0 0 6.6 6.6l2.2-2.2c.3-.3.7-.4 1-.2 1.1.4 2.3.6 3.6.6.6 0 1 .4 1 1V20c0 .6-.4 1-1 1A17 17 0 0 1 3 4c0-.6.4-1 1-1h3.5c.6 0 1 .4 1 1 0 1.3.2 2.5.6 3.6.1.3 0 .7-.2 1z"/></svg>
      <span>(832) 555-0147</span>
    </li>
    <li class="contact__item">
      <svg class="contact__icon" viewBox="0 0 24 24" aria-hidden="true"><path d="M2 5h20v14H2z M3.5 6.5 12 13l8.5-6.5" fill="none" stroke="#33a6d7" stroke-width="2.4"/></svg>
      <span>maren@netclaritypartners.example</span>
    </li>
    <li class="contact__item">
      <svg class="contact__icon" viewBox="0 0 24 24" aria-hidden="true"><path d="M12 2a7 7 0 0 0-7 7c0 5.2 7 13 7 13s7-7.8 7-13a7 7 0 0 0-7-7zm0 9.5A2.5 2.5 0 1 1 12 6.5a2.5 2.5 0 0 1 0 5z"/></svg>
      <span>4517 Pellam Rd., #349, Houston, TX 77348</span>
    </li>
  </ul>
</section>

<section class="card card--back" aria-label="Business card back">
  <div class="back__portrait" role="img" aria-label="Portrait photo of Maren Falstead"></div>
  <div class="back__brand">
    <div class="brand-name">Net Clarity Partners</div>
    <div class="brand-tagline">Smart Marketing for Law Firms</div>
  </div>
  <div class="back__notch"></div>
  <div class="back__rule"></div>
  <div class="back__band">
    <span class="back__url">www.netclaritypartners.example</span>
  </div>
</section>

</body>
</html>
```